Book cover for publishing doctoral research about various national styles of piano playing.

I need a book cover for a publication of a doctoral research with regard to styles of piano performance characteristic to various nations.

Any images or graphics are optional, typography seems most important, but please feel free to be creative.

I attach the barcode, qsr and publisher's logo in the next few days. (Logo is still being designed).

For various reasons the size of the book is not completely decided yet. Please create your design in 7" x 10", but if at all possible, I would like to ask for files of two sizes, also including 8.5" x 11" in the final submission.

I am looking for a design that looks professional, probably simple, but I am open to any suggestions.
Updates

Dear Designers,I would like to thank you all for participation and submitting so many high-quality designs.My final decision was based on the feedback I received from my professional colleagues and potential readers.I would like to wish you all the best for the future.Best wishes,Radosław Added Monday, December 21, 2015

Target Market(s)

Pianists, students, music professionals

Industry/Entity Type

Publishing

Requirements
Must have
• Title: Tracing Regional Keyboard Lineages
• Subtitle: Origins and legacies
• Author: Radosław Kępiński
• Space for my logo on the front page and the spine.
• On the back page, please include some space for a short biography, 'barcode' and 'qsr' code.
• Please include whatever else you consider necessary.
Nice to have
• Would it be possible to use the same cover to a e-book edition?

```html
<!DOCTYPE html>
<html lang="en">
<head>
<meta charset="utf-8">
<title>Tracing Regional Keyboard Lineages — Book Cover</title>
<link rel="stylesheet" href="https://fonts.googleapis.com/css2?family=EB+Garamond:wght@400;600&display=swap">
<style>
  :root {
    --backdrop: #f2f2f2;
    --cover: #ffffff;
    --ink: #2b2b2b;
    --ink-soft: #3a3a3a;
    --piano-dark: #141414;
    --piano-mid: #3c3c3c;
    --logo-disc: #dcdcdc;
    --logo-ink: #1e1e1e;
  }
  * { box-sizing: border-box; margin: 0; padding: 0; }
  html, body {
    width: 1200px;
    height: 942px;
    overflow: hidden;
    background: var(--backdrop);
  }
  .book-cover {
    position: absolute;
    left: 285px;
    top: 21px;
    width: 630px;
    height: 900px;
    background: var(--cover);
    box-shadow: 0 2px 10px rgba(0,0,0,0.08);
    font-family: "EB Garamond", "Times New Roman", serif;
    color: var(--ink);
    text-align: center;
  }
  .title-block {
    position: absolute;
    top: 110px;
    left: 0;
    width: 100%;
    line-height: 0.9;
  }
  .title-line { display: block; font-weight: 400; letter-spacing: 0.01em; }
  .title-line--1 { font-size: 28px; }
  .title-line--2 { font-size: 42px; }
  .title-line--3 { font-size: 60px; }
  .title-line--4 { font-size: 74px; }
  .subtitle {
    display: block;
    margin-top: 6px;
    font-size: 30px;
    color: var(--ink-soft);
    line-height: 1;
  }
  .cover-art {
    position: absolute;
    left: 200px;
    top: 380px;
    width: 230px;
    height: 250px;
    background: radial-gradient(ellipse at 55% 40%, var(--piano-mid) 0%, var(--piano-dark) 70%);
    border-radius: 6px;
  }
  .author {
    position: absolute;
    top: 735px;
    left: 0;
    width: 100%;
  }
  .author-label { display: block; font-size: 17px; color: var(--ink-soft); }
  .author-name { display: block; font-size: 27px; margin-top: 2px; }
  .publisher-mark {
    position: absolute;
    right: 38px;
    top: 590px;
    width: 76px;
    height: 76px;
    border-radius: 50%;
    background: var(--logo-disc);
    display: flex;
    align-items: center;
    justify-content: center;
    font-size: 18px;
    font-weight: 600;
    color: var(--logo-ink);
  }
</style>
</head>
<body>
  <main class="book-cover">
    <h1 class="title-block">
      <span class="title-line title-line--1">TRACING</span>
      <span class="title-line title-line--2">REGIONAL</span>
      <span class="title-line title-line--3">KEYBOARD</span>
      <span class="title-line title-line--4">LINEAGES</span>
      <span class="subtitle">Origins and legacies</span>
    </h1>
    <div class="cover-art" role="img" aria-label="Photograph of a black grand piano with its lid open and a piano bench"></div>
    <div class="publisher-mark">LOGO</div>
    <p class="author">
      <span class="author-label">Author:</span>
      <span class="author-name">Radosław Kępiński</span>
    </p>
  </main>
</body>
</html>
```